K&R Flame Guard Supply Inc. needs an updated/new website design

I would like the customer to be able to see who we are, where are are, what we do and areas we cover on the first page. I would like something modern but professional. The other fire safety companies out there have very boring & unappealing websites. I want mine seem like we've got it together and to be above average in comparison. I would like the colors to go with our logo and would like to incorporate somewhere that we have been in business for over 30 years, we are family owned and operated and that we provide service to all of central Florida from Tampa to Titusville and all of Brevard county (we can take out the" all of Brevard county" but keep the " All of Central Florida from Tampa to Titusville" and just add all counties we service to the very bottom too). We are a residential and commercial fire safety equipment company. We do sales, service and installation for fire extinguishers, emergency/exit lighting, kitchen fire suppression systems, fire alarms & fire extinguisher cabinets.I have also attached some pictures that you can use to incorporate any way you would like. Here's our current website (awful I know) to get information from if needed. kandrflameguard.example

Target Market(s)

Restaurants, hotels, vacation rental properties & small businesses. Every business is required to have a fire extinguisher and exit lighting.

Industry/Entity Type

Fire Safety

Number of Pages Required

1 page

Font styles to use
Other font styles liked:
• I'm open to your suggestions

Colors

Designer to choose colors to be used in the design.

Requirements
Must have
• I would like the customer to be able to see who we are, where are are, what we do and areas we cover on the first page. I would like the colors to go with our logo and would like to incorporate somewhere that we have been in business for over 30 years, we are family owned and operated and that we provide service to all of central Florida from Tampa to Titusville and all of Brevard county (we can take out the" all of Brevard county" but keep the " All of Central Florida from Tampa to Titusville" and just add all counties we service to the very bottom too)
Nice to have
• Modern with high quality pictures
• I love the raised logo that I added in the attachments. If you could make the logo look like that in incorporate it as one of the first things you see that would be awesome!
• I would eventually like to have a portfolio of work completed on an additional page.
Should not have
• boring outdated look

```html
<!DOCTYPE html>
<html lang="en">
<head>
<meta charset="utf-8">
<title>K&amp;R Flame Guard Supply Inc.</title>
<link href="https://fonts.googleapis.com/css2?family=Roboto:ital,wght@0,300;0,400;0,500;0,700;0,900;1,400&family=Roboto+Condensed:wght@300;400;700&display=swap" rel="stylesheet">
<style>
:root{
  --gold:#f2b203;
  --amber:#e39a05;
  --red:#e8321e;
  --ink:#1c1a17;
  --dark:#232323;
  --text:#333;
  --muted:#777;
  --light:#f0f0f0;
  --white:#fff;
}
*{margin:0;padding:0;box-sizing:border-box}
html,body{width:1200px;height:2975px;overflow:hidden}
body{position:relative;background:var(--white);font-family:"Roboto",Arial,sans-serif;color:var(--text)}
.abs{position:absolute}

/* hero */
.hero{left:0;top:0;width:1200px;height:569px;background:linear-gradient(180deg,#2a3f8a 0%,#3c4d96 35%,#5a4e7a 60%,#a0643d 80%,#3a3040 100%)}
.phone-bar{right:0;top:0;width:328px;height:30px;background:var(--gold);clip-path:polygon(18px 0,100% 0,100% 100%,0 100%);display:flex;align-items:center;justify-content:center;gap:10px;font:700 18px "Roboto",sans-serif;color:var(--ink)}
.brand{left:160px;top:34px;display:flex;align-items:center;gap:10px;color:var(--white);font:700 22px/1.15 "Roboto",sans-serif;width:260px}
.brand-dot{width:34px;height:34px;border-radius:50%;background:var(--gold);flex:none}
.hero-title{right:165px;top:176px;text-align:right;color:var(--white)}
.hero-title .kicker{font:300 31px "Roboto Condensed",sans-serif;text-align:center;letter-spacing:.5px}
.hero-title h1{font:700 42px "Roboto Condensed",sans-serif;letter-spacing:.3px;margin-top:4px}
.hero-stripe{left:0;top:532px;width:387px;height:37px;background:var(--gold);clip-path:polygon(0 0,350px 0,100% 100%,0 100%)}

/* nav */
.nav{left:0;top:569px;width:1200px;height:42px;background:var(--ink)}
.nav ul{position:absolute;left:160px;top:0;height:42px;display:flex;align-items:center;gap:38px;list-style:none}
.nav li{font:500 13px "Roboto",sans-serif;color:var(--white)}
.socials{display:flex;gap:10px}
.nav .socials{position:absolute;right:164px;top:11px}
.social{width:20px;height:20px;border-radius:50%;border:1.5px solid #cfcfcf}

/* intro cards */
.intro{left:0;top:611px;width:1200px;height:476px;background:var(--light)}
.card{top:43px;width:278px;height:391px;background:var(--white)}
.card-photo{height:159px;width:100%}
.card-label{height:44px;background:var(--gold);position:relative;text-align:center;font:500 17px/44px "Roboto",sans-serif;color:var(--ink)}
.card-label::after{content:"";position:absolute;left:50%;bottom:-9px;margin-left:-9px;border:9px solid transparent;border-bottom:0;border-top-color:var(--gold)}
.card p{margin:24px 16px 0;font:400 10.5px/1.6 "Roboto",sans-serif;color:var(--muted);text-align:center}
.btn-dark{display:inline-flex;align-items:center;gap:6px;background:var(--ink);color:var(--white);font:500 11px "Roboto",sans-serif;padding:9px 14px}
.card .btn-dark{position:absolute;left:50%;transform:translateX(-50%);bottom:28px}

/* welcome */
.welcome{left:160px;top:1150px;width:560px}
.welcome .pre{font:400 27px "Roboto",sans-serif;color:var(--ink)}
.welcome h2{font:700 30px "Roboto",sans-serif;color:var(--red);margin-top:-2px}
.welcome .tag{font:400 13px "Roboto",sans-serif;color:var(--muted);margin:4px 0 10px}
.welcome p{font:400 10.5px/1.7 "Roboto",sans-serif;color:var(--text)}
.btn-gold{left:160px;top:1354px;width:147px;height:34px;background:var(--gold);box-shadow:0 3px 0 #b98500;display:flex;align-items:center;justify-content:center;gap:7px;font:700 13px "Roboto",sans-serif;color:var(--ink)}
.portrait-back{left:813px;top:1122px;width:224px;height:256px;background:var(--ink)}
.portrait{left:763px;top:1150px;width:241px;height:256px;border:4px solid var(--gold);background:var(--white);padding:6px}
.portrait div{width:100%;height:100%;background:linear-gradient(160deg,#e9e6e0,#b9b2a6 55%,#3b3d43)}

/* services */
.services{left:0;top:1452px;width:1200px;height:214px;background:var(--gold);text-align:center}
.services svg{margin-top:24px}
.services h2{font:700 36px "Roboto Condensed",sans-serif;color:var(--ink)}
.services h2::after{content:"";display:block;width:236px;height:2px;background:var(--ink);margin:2px auto 0}
.services p{font:400 12.5px/1.55 "Roboto",sans-serif;color:var(--ink);width:800px;margin:10px auto 0}
.tiles{left:0;top:1666px;width:1200px;height:254px;display:flex}
.tile{flex:1;position:relative;border-right:2px solid var(--white)}
.tile:last-child{border-right:0}
.tile span{position:absolute;left:0;right:0;bottom:20px;text-align:center;font:700 18px "Roboto Condensed",sans-serif;color:var(--white);text-shadow:0 1px 3px rgba(0,0,0,.7)}

/* testimonials */
.testi-head{left:300px;top:1970px;width:600px;display:flex;align-items:center;gap:16px}
.testi-head i{flex:1;height:5px;border-top:1px solid #aaa;border-bottom:1px solid #aaa}
.testi-head h2{font:700 34px "Roboto Condensed",sans-serif;color:var(--ink)}
.quote{top:2090px;width:267px;height:197px;background:#ececec;text-align:center}
.avatar{position:absolute;left:50%;top:-34px;margin-left:-35px;width:70px;height:70px;border-radius:50%;border:3px solid var(--white);background:linear-gradient(160deg,#cfd6df,#8a8f98)}
.quote p{margin:58px 34px 0;font:italic 400 10.5px/1.6 "Roboto",sans-serif;color:#555}
.quote .who{margin-top:14px;font:400 10px "Roboto",sans-serif;color:#555}
.stars{margin-top:4px;color:var(--amber);font-size:11px;letter-spacing:1px}

/* consult */
.consult{left:0;top:2376px;width:1200px;height:267px;background:linear-gradient(180deg,#e2e2e2,#cfcfcf 70%,#d8d8d8)}
.consult-text{left:160px;top:2438px}
.consult-text h3{font:700 22px "Roboto Condensed",sans-serif;color:var(--ink)}
.consult-text p{font:400 12px "Roboto",sans-serif;color:var(--text);margin-top:2px}
.btn-consult{left:765px;top:2435px;width:272px;height:46px;background:var(--ink);color:var(--white);display:flex;align-items:center;justify-content:center;gap:10px;font:700 15px "Roboto Condensed",sans-serif}

/* footer */
.footer{left:0;top:2643px;width:1200px;height:332px;background:var(--dark)}
.newsletter{left:160px;top:2554px;width:877px;height:175px;background:var(--amber);text-align:center}
.newsletter h3{font:700 24px "Roboto Condensed",sans-serif;color:var(--white);margin-top:24px}
.newsletter p{font:400 11.5px "Roboto",sans-serif;color:var(--white);margin-top:4px}
.signup{display:flex;justify-content:center;margin-top:18px}
.signup span{width:352px;height:40px;background:var(--white);font:400 10px/40px "Roboto",sans-serif;color:#999;text-align:left;padding-left:14px}
.signup b{width:110px;height:40px;background:var(--ink);color:var(--white);font:500 14px/40px "Roboto",sans-serif}
.join{left:0;top:2748px;width:1200px;text-align:center;font:500 36px "Roboto",sans-serif;color:var(--white)}
.footer-social{left:0;top:2820px;width:1200px;display:flex;justify-content:center;gap:16px}
.footer-social .social{width:32px;height:32px}
.footer-links{left:0;top:2906px;width:1200px;display:flex;justify-content:center;gap:22px;list-style:none;font:500 10.5px "Roboto",sans-serif;color:#bbb}
.footer-links li+li::before{content:"|";margin-right:22px;color:#777}
.copyright{left:0;top:2938px;width:1200px;text-align:center;font:400 10px "Roboto",sans-serif;color:#888}
</style>
</head>
<body>

<section class="abs hero" role="img" aria-label="Night city skyline reflected in the water"></section>
<div class="abs phone-bar">
  <svg width="18" height="18" viewBox="0 0 24 24"><circle cx="12" cy="12" r="11" fill="none" stroke="#1c1a17" stroke-width="2"/><path d="M8 6.5l2 .3 1 2.7-1.4 1.2a8 8 0 0 0 3.7 3.7l1.2-1.4 2.7 1 .3 2a1.6 1.6 0 0 1-1.7 1.4A10 10 0 0 1 6.6 8.2 1.6 1.6 0 0 1 8 6.5z" fill="#1c1a17"/></svg>
  1-407-555-0188
</div>
<div class="abs brand"><span class="brand-dot"></span><span>K&amp;R Flame Guard Supply Inc.</span></div>
<div class="abs hero-title">
  <div class="kicker">DEDICATED TO</div>
  <h1>PROTECTING LIFE AND PROPERTY</h1>
</div>
<div class="abs hero-stripe"></div>

<nav class="abs nav">
  <ul><li>HOME</li><li>SERVICES</li><li>TESTIMONIALS</li><li>JOBS</li><li>CONTACT US</li></ul>
  <div class="socials"><span class="social"></span><span class="social"></span><span class="social"></span><span class="social"></span><span class="social"></span></div>
</nav>

<section class="abs intro">
  <article class="abs card" style="left:160px">
    <div class="card-photo" role="img" aria-label="Technician working on an electrical fire alarm panel" style="background:linear-gradient(135deg,#d8d8d8,#5a5e66 55%,#2a2a2e)"></div>
    <div class="card-label">WHO WE ARE</div>
    <p>Lorem Ipsum is simply dummy text of the printing and typesetting industry. Lorem Ipsum has been the industry's standard dummy text ever since the type and scrambled it to make a type specimen book. Layout including versions of Lorem Ipsum.</p>
    <span class="btn-dark">READ MORE <svg width="10" height="10" viewBox="0 0 10 10"><circle cx="5" cy="5" r="5" fill="#fff"/><path d="M4 2.8 6.2 5 4 7.2" stroke="#1c1a17" stroke-width="1.4" fill="none"/></svg></span>
  </article>
  <article class="abs card" style="left:458px">
    <div class="card-photo" role="img" aria-label="Technician inspecting a fire extinguisher in a wall cabinet" style="background:linear-gradient(135deg,#f2f2f2,#c9c9c9 55%,#3a3a3a)"></div>
    <div class="card-label">WHERE WE ARE</div>
    <p>Lorem Ipsum is simply dummy text of the printing and typesetting industry. Lorem Ipsum has been the industry's standard dummy text ever since the type and scrambled it to make a type specimen book. Layout including versions of Lorem Ipsum.</p>
    <span class="btn-dark">READ MORE <svg width="10" height="10" viewBox="0 0 10 10"><circle cx="5" cy="5" r="5" fill="#fff"/><path d="M4 2.8 6.2 5 4 7.2" stroke="#1c1a17" stroke-width="1.4" fill="none"/></svg></span>
  </article>
  <article class="abs card" style="left:760px">
    <div class="card-photo" role="img" aria-label="Close-up of a red fire alarm device with white lettering" style="background:linear-gradient(135deg,#c92828,#e24a3c 50%,#e6e6e6)"></div>
    <div class="card-label">WHAT WE DO</div>
    <p>Lorem Ipsum is simply dummy text of the printing and typesetting industry. Lorem Ipsum has been the industry's standard dummy text ever since the type and scrambled it to make a type specimen book. Layout including versions of Lorem Ipsum.</p>
    <span class="btn-dark">READ MORE <svg width="10" height="10" viewBox="0 0 10 10"><circle cx="5" cy="5" r="5" fill="#fff"/><path d="M4 2.8 6.2 5 4 7.2" stroke="#1c1a17" stroke-width="1.4" fill="none"/></svg></span>
  </article>
</section>

<section class="abs welcome">
  <div class="pre">WELCOME TO</div>
  <h2>FLAME GUARD SUPPLY INC.</h2>
  <div class="tag">DEDICATED TO PROTECTING LIFE AND PROPERTY</div>
  <p>We have been providing fire protection to Central Florida for over 30 years! K&amp;R Flame Guard is family owned and operated. We provide quality service, professional fire protection and life safety to meet the needs of our community. We provide residential and commercial fire protection to all of Brevard County and Central Florida from Tampa to Titusville. Our staff is exceptionally knowledgeable in fire safety and protection. Please feel free to contact us with any questions or concerns.</p>
</section>
<div class="abs btn-gold"><svg width="14" height="11" viewBox="0 0 14 11"><rect width="14" height="11" rx="1" fill="#1c1a17"/><path d="M1 1.5 7 6l6-4.5" stroke="#f2b203" stroke-width="1.2" fill="none"/></svg>CONTACT US</div>
<div class="abs portrait-back"></div>
<div class="abs portrait"><div role="img" aria-label="Smiling firefighter in uniform standing in a station"></div></div>

<section class="abs services">
  <svg width="36" height="46" viewBox="0 0 36 46"><path d="M18 2c2 8 12 14 12 26a12 12 0 0 1-24 0c0-6 3-10 6-13 0 5 2 8 4 9-1-8 2-15 2-22z" fill="#1c1a17"/><path d="M18 26c2 3 5 5 5 10a5 5 0 0 1-10 0c0-3 2-5 5-10z" fill="#f2b203"/></svg>
  <h2>OUR SERVICES</h2>
  <p>Lorem Ipsum is simply dummy text of the printing and typesetting industry. Lorem Ipsum has been the industry's standard dummy text ever an unknown printer took a galley of type and scrambled it to make a type specimen book.</p>
</section>
<div class="abs tiles">
  <div class="tile" role="img" aria-label="Illuminated exit signs in a dark corridor" style="background:linear-gradient(135deg,#5a0d0d,#1e1a1a 50%,#0e3a22)"><span>EXIT LIGHTING</span></div>
  <div class="tile" role="img" aria-label="Red emergency alarm light on a wall" style="background:linear-gradient(135deg,#b82020,#e8e2dc 55%,#9a9a9a)"><span>EMERGENCY LIGHTING</span></div>
  <div class="tile" role="img" aria-label="Two men examining a fire extinguisher" style="background:linear-gradient(135deg,#d9dde3,#8d95a0 55%,#3d4550)"><span>FIRE EXTINGUISHER SALES</span></div>
  <div class="tile" role="img" aria-label="Row of red fire suppression cylinders" style="background:linear-gradient(135deg,#9ea4a8,#c1272d 50%,#6a1618)"><span>FIRE SUPPRESSION SYSTEMS</span></div>
</div>

<div class="abs testi-head"><i></i><h2>TESTIMONIALS</h2><i></i></div>
<article class="abs quote" style="left:159px">
  <span class="avatar" role="img" aria-label="Customer portrait"></span>
  <p>“ industry's printer took a galley of type and scrambled it to make a type also transfers more recently with desktop publishing software like page layout including versions ”</p>
  <div class="who">__ Daniel Hayes</div><div class="stars">★★★★★</div>
</article>
<article class="abs quote" style="left:464px">
  <span class="avatar" role="img" aria-label="Customer portrait"></span>
  <p>“ industry's printer took a galley of type and scrambled it to make a type also transfers more recently with desktop publishing software like page layout including versions ”</p>
  <div class="who">__ Rosa Mendez</div><div class="stars">★★★★★</div>
</article>
<article class="abs quote" style="left:770px">
  <span class="avatar" role="img" aria-label="Customer portrait"></span>
  <p>“ industry's printer took a galley of type and scrambled it to make a type also transfers more recently with desktop publishing software like page layout including versions ”</p>
  <div class="who">__ Daniel Hayes</div><div class="stars">★★★★★</div>
</article>

<section class="abs consult" role="img" aria-label="Faded grey city skyline backdrop"></section>
<div class="abs consult-text">
  <h3>CONSULT OUR SERVICE</h3>
  <p>Lorem Ipsum is simply dummy text of the printing and typesetting industry Lorem Ipsum.</p>
</div>
<div class="abs btn-consult">GET FREE CONSULTATION <svg width="9" height="13" viewBox="0 0 9 13"><path d="M2 1.5 7 6.5 2 11.5" stroke="#fff" stroke-width="2.2" fill="none"/></svg></div>

<footer class="abs footer"></footer>
<section class="abs newsletter">
  <h3>NEWSLETTER</h3>
  <p>Enter your email adress for getting updates</p>
  <div class="signup"><span>Enter your email id</span><b>Subscribe</b></div>
</section>
<div class="abs join">Join the conversation</div>
<div class="abs footer-social"><span class="social"></span><span class="social"></span><span class="social"></span><span class="social"></span><span class="social"></span></div>
<ul class="abs footer-links"><li>HOME</li><li>SERVICES</li><li>TESTIMONIALS</li><li>JOBS</li><li>CONTACT US</li></ul>
<div class="abs copyright">© 2018 All rights reserved kandrflameguard.example</div>

</body>
</html>
```